Lagerverkauf
Zielgruppe
Textil Großhandel mit bekleidung bekannter Marken wie Varnek, Tolmsey, Lumo jeans etc..
Aufgabenstellung
Flyer DIn lang für einen Lagerverkauf von markenbekleidung, einfach gehalten, sehr clean, kein schnick schnack..
Marken: Tolmsey, Varnek, Lumo jeans, Zib, Fentholt, Pilkå, Morten Blasé, Wrenz...etc
Inhalt Verkauf von z.B 4.09.2014 - 6.09.2014
Öffnungszeiten Do - 10 - 18 uhr, Fr - 10 - 18 Uhr, Sa 10 - 16 Uhr
Adresse Platzhalter

```html
<!DOCTYPE html>
<html lang="de">
<head>
<meta charset="utf-8">
<title>Lagerverkauf</title>
<link rel="stylesheet" href="https://fonts.googleapis.com/css2?family=League+Spartan:wght@500;800;900&display=swap">
<style>
  :root {
    --ink: #000;
    --paper: #fff;
    --brand-ink: #2a2a2a;
  }
  html, body {
    margin: 0;
    padding: 0;
    overflow: hidden;
    background: var(--paper);
  }
  .flyer {
    position: relative;
    width: 1200px;
    height: 600px;
    overflow: hidden;
    background: var(--paper);
    font-family: "League Spartan", sans-serif;
    color: var(--ink);
  }
  .headline {
    position: absolute;
    left: 0;
    top: 0;
    width: 1200px;
    height: 360px;
  }
  .headline .solid {
    font-family: "League Spartan", sans-serif;
    font-weight: 900;
    font-size: 340px;
    fill: var(--ink);
  }
  .headline .outline {
    font-family: "League Spartan", sans-serif;
    font-weight: 900;
    font-size: 258px;
    font-kerning: none;
    letter-spacing: 30px;
    fill: var(--paper);
    stroke: var(--ink);
    stroke-width: 6;
    stroke-linejoin: miter;
  }
  .rule {
    position: absolute;
    left: 0;
    width: 1200px;
    height: 5px;
    background: var(--ink);
  }
  .rule--top { top: 365px; }
  .rule--bottom { top: 518px; }
  .details {
    position: absolute;
    left: 18px;
    top: 386px;
    margin: 0;
    font-weight: 800;
    font-size: 34px;
    line-height: 44px;
    letter-spacing: -0.2px;
  }
  .details p { margin: 0; white-space: nowrap; }
  .tagline {
    position: absolute;
    right: 8px;
    top: 380px;
    margin: 0;
    font-weight: 800;
    font-size: 28px;
    letter-spacing: 0.4px;
  }
  .brands {
    position: absolute;
    left: 0;
    top: 530px;
    width: 1200px;
    height: 66px;
    margin: 0;
    padding: 0;
    list-style: none;
  }
  .brand {
    position: absolute;
    top: 14px;
    font-weight: 500;
    font-size: 29px;
    line-height: 38px;
    color: var(--brand-ink);
    white-space: nowrap;
  }
</style>
</head>
<body>
<main class="flyer">
  <svg class="headline" viewBox="0 0 1200 360" aria-label="Lagerverkauf">
    <g class="solid">
      <text x="-8" y="168" textLength="112" lengthAdjust="spacingAndGlyphs">L</text>
      <text x="236" y="168" textLength="168" lengthAdjust="spacingAndGlyphs">A</text>
      <text x="542" y="168" textLength="164" lengthAdjust="spacingAndGlyphs">G</text>
      <text x="861" y="168" textLength="131" lengthAdjust="spacingAndGlyphs">E</text>
      <text x="1100" y="168" textLength="140" lengthAdjust="spacingAndGlyphs">R</text>
    </g>
    <text class="outline" x="-6" y="348" textLength="1212" lengthAdjust="spacingAndGlyphs">VERKAUF</text>
  </svg>

  <div class="rule rule--top"></div>

  <p class="tagline">VON MARKENBEKLEIDUNG</p>

  <section class="details">
    <p>Verkauf von z.B 4.09.2014 - 6.09.2014</p>
    <p>Öffnungszeiten Do - 10 - 18 uhr, Fr - 10 - 18 Uhr, Sa 10 - 16 Uhr</p>
    <p>Adresse:</p>
  </section>

  <div class="rule rule--bottom"></div>

  <ul class="brands">
    <li class="brand" style="left:31px">Morten Blasé</li>
    <li class="brand" style="left:262px">Fentholt</li>
    <li class="brand" style="left:385px">Wrenz</li>
    <li class="brand" style="left:545px">Lumo jeans</li>
    <li class="brand" style="left:745px">Varnek</li>
    <li class="brand" style="left:915px">Tolmsey</li>
    <li class="brand" style="left:1075px">Pilkå</li>
  </ul>
</main>
</body>
</html>
```